Large Christian Church organization website design

This website design is an advanced design ultimately requiring design for at least 4 pages, but starting with only one.

I am looking for an "award winning" design. I have made this easy as I have the functionality and general flow prototyped in an HTML prototype. I recorded videos to explain these in depth and will attach the HTML prototype as well.

The design must focused on connecting with people who need physical, emotional or spiritual help. It will be a website designed to meet people where they are and to help bring them along in there relationship to God.

Please work on this design only if you have a heart for people connecting with Christians and God.

A couple designers have asked me about the brief... did you have trouble downloading the brief for this project from this page:

If so, perhaps you can email me directly and I can send to you... you can email me: wendell@brightkettle.org.
Also, would love to know if you still plan on creating a design for this project, thanks!

Reason: Still looking for a design that matches the functionality we need and provides a fantastic home run look and feel that is warm, inviting and friendly...

Reason: Need more time to provide feedback, request edits...

See creative brief

Church

• The latest creative brief can be found here:

https://files.quorvapad.net/a/veltromesh.com/document/d/8Z3kQpLm2VxT7nRw4YsBcE9hJdGf5aUo0iKtNqWeXrZ/edit?hl=en_US#bookmark=id.kqmztwlsoyve

```html
<!DOCTYPE html>
<html lang="en">
<head>
<meta charset="utf-8">
<title>North Texas Church Network</title>
<link href="https://fonts.googleapis.com/css2?family=Arimo:wght@400;700&family=Libre+Caslon+Text:wght@700&display=swap" rel="stylesheet">
<style>
:root{
  --bar:#262626;
  --red-deep:#6e1409;
  --red:#a3220f;
  --red-line:#c23418;
  --gold:#f2c200;
  --band:#121212;
  --white:#ffffff;
  --panel-line:#d4d4d4;
  --sky:#2fb4ea;
  --link:#1a7bd6;
  --link2:#2fa8e6;
  --ink:#222;
  --foot:#e7e7e7;
}
*{margin:0;padding:0;box-sizing:border-box}
html,body{width:1200px;height:750px;overflow:hidden}
body{position:relative;font-family:Arimo,Arial,sans-serif;background:var(--white);color:var(--ink)}
.abs{position:absolute}

/* top bar */
.topbar{left:0;top:0;width:1200px;height:32px;background:linear-gradient(#303030,#1d1d1d);border-bottom:1px solid var(--red-line)}
.home-icon{left:226px;top:5px}
.menu-btn{top:6px;height:21px;border-radius:2px;color:#fff;font-size:7.5px;font-weight:700;letter-spacing:.2px;display:flex;align-items:center;justify-content:space-between;padding:0 5px;white-space:nowrap;text-transform:uppercase}
.menu-btn i{width:8px;height:8px;border-radius:50%;background:rgba(0,0,0,.5);display:block;flex:none}
.menu-welcome{left:263px;width:87px;background:linear-gradient(#e0261a,#a8120a);border:1px solid #5a0a05}
.menu-church{left:357px;width:83px;background:linear-gradient(#5bbbf0,#2a86c8);border:1px solid #1b4f78}
.nav{left:447px;top:5px;width:391px;height:23px;background:linear-gradient(#5a5a5a,#3b3b3b);border:1px solid #222;border-radius:2px;display:flex}
.nav a{flex:1;color:#eee;text-decoration:none;font-size:11px;display:flex;align-items:center;justify-content:center;border-right:1px solid #2c2c2c}
.nav a:last-child{border-right:0}
.social{left:848px;top:8px;display:flex;gap:6px}
.social span{width:16px;height:16px;border-radius:3px;display:block}

/* hero */
.redband{left:0;top:33px;width:1200px;height:261px;background:radial-gradient(ellipse at 50% 40%,var(--red),var(--red-deep) 75%)}
.hero{left:226px;top:40px;width:750px;height:250px;overflow:hidden;
  background:
    radial-gradient(ellipse 30% 40% at 20% 65%,rgba(45,120,95,.9),rgba(45,120,95,0)),
    radial-gradient(ellipse 35% 45% at 60% 60%,rgba(40,130,105,.9),rgba(40,130,105,0)),
    radial-gradient(ellipse 25% 30% at 85% 55%,rgba(35,110,90,.85),rgba(35,110,90,0)),
    radial-gradient(ellipse 20% 18% at 45% 30%,rgba(60,38,28,.9),rgba(60,38,28,0)),
    radial-gradient(ellipse 20% 18% at 75% 28%,rgba(55,35,25,.9),rgba(55,35,25,0)),
    linear-gradient(#9c6a55,#6a4636 25%,#3d5048 50%,#24493c 75%,#2a1e18);
  box-shadow:0 0 12px rgba(0,0,0,.5)}
.hero-caption{position:absolute;left:0;top:172px;height:38px;padding:0 40px 0 13px;background:linear-gradient(90deg,rgba(0,0,0,.6),rgba(0,0,0,.4) 85%,rgba(0,0,0,0));font-family:"Libre Caslon Text",Georgia,serif;font-weight:700;font-size:23px;color:var(--gold);display:flex;align-items:center;white-space:nowrap}
.dots{left:592px;top:273px;display:flex;gap:4px}
.dots span{width:10px;height:10px;border-radius:50%;background:#fff;display:block}
.dots span:first-child{background:transparent;border:2px solid #fff}
.bubble{background:linear-gradient(#fff,#e2e2e2);border-radius:5px;font-size:10px;color:#222;display:flex;align-items:center;justify-content:center;box-shadow:0 1px 3px rgba(0,0,0,.4)}
.bubble-home{left:169px;top:37px;width:56px;height:26px}
.bubble-tour{left:887px;top:40px;width:82px;height:24px}

/* tiles */
.band{left:0;top:294px;width:1200px;height:131px;background:var(--band)}
.tile{top:302px;width:107px;height:112px;background:linear-gradient(#2a2a2a,#161616);border:1px solid #3c3c3c;border-radius:3px}
.tile .pic{position:absolute;left:4px;top:4px;width:97px;height:76px}
.tile .label{position:absolute;left:5px;right:3px;top:84px;height:24px;color:#fff;font-size:8.6px;font-weight:700;display:flex;align-items:center;line-height:1.25;white-space:nowrap}
.tile .label.center{justify-content:center;text-align:center}

/* welcome panel */
.panel{left:225px;top:432px;width:752px;height:176px;background:var(--white);border:1px solid var(--panel-line);border-radius:3px}
.panel-head{position:absolute;left:0;top:0;width:100%;height:28px;background:linear-gradient(#f4f4f4,#e8e8e8);border-bottom:1px solid var(--panel-line);font-size:14px;padding-left:8px;display:flex;align-items:center;white-space:pre}
.arrow{top:520px}
.card{top:467px;width:167px}
.card .frame{width:167px;height:82px;border:1px solid #d8d8d8;background:#fff;padding:4px;box-shadow:0 1px 2px rgba(0,0,0,.15)}
.card .pic{position:relative;width:100%;height:100%}
.card .tag{position:absolute;left:0;bottom:0;width:125px;height:20px;background:linear-gradient(90deg,var(--sky),rgba(47,180,234,.85) 80%,rgba(47,180,234,0));color:#fff;font-size:10px;font-weight:700;display:flex;align-items:center;padding-left:3px;white-space:nowrap}
.learn{position:absolute;left:1px;top:90px}
.connect{position:absolute;left:1px;top:120px;font-size:10.5px;color:#333;white-space:nowrap}
.connect .g{color:var(--link)}
.connect .c{color:var(--link2)}

/* footer bar */
.footbar{left:0;top:621px;width:1200px;height:34px;background:linear-gradient(#2e2e2e,#1c1c1c)}
.nearest{left:225px;top:630px;color:#ddd;font-size:7.5px;font-weight:700;line-height:10px}
.locate{left:279px;top:628px;width:152px;height:21px;background:#2b2b2b;border:1px solid #111;color:#ccc;font-size:9px;display:flex;align-items:center;gap:6px;padding-left:7px}
.locate i{width:9px;height:9px;border-radius:50%;border:1.5px solid #666;display:block}
.globe{left:439px;top:628px;width:35px;height:21px;background:#333;border:1px solid #111}
.community{left:492px;top:635px;color:#aaa;font-size:9.5px;letter-spacing:.6px;white-space:nowrap}
.community b{color:#ddd;font-size:12px;letter-spacing:0;margin-left:6px}
.account{left:778px;top:628px;width:190px;height:21px;background:linear-gradient(90deg,#111,#000);color:#fff;font-size:10px;display:flex;align-items:center;padding-left:8px}
.signin{left:914px;top:629px;width:53px;height:19px;background:linear-gradient(#bbb,#777);color:#fff;font-size:11px;font-weight:700;display:flex;align-items:center;justify-content:center;border-radius:2px}

/* footer */
.foot{left:0;top:655px;width:1200px;height:95px;background:var(--foot)}
.brand{left:225px;top:668px;width:52px;display:flex;flex-direction:column;align-items:center;gap:5px;color:#c23418;font-size:9.5px;font-weight:700}
.brand span{width:16px;height:16px;background:#c23418;display:block}
.divider{left:283px;top:659px;width:1px;height:88px;background:#aaa}
.col{top:664px;font-size:10.4px;line-height:13.3px;color:#333;white-space:nowrap}
.col h4{font-size:10.4px;font-weight:400;color:#222}
.suggest{left:784px;top:667px;font-size:10.5px}
.msg{left:782px;top:684px;width:186px;height:40px;background:#cfcfcf;border:1px solid #aaa;color:#888;font-size:9px;font-style:italic;padding:5px}
.send{left:927px;top:730px;width:40px;height:16px;background:linear-gradient(#444,#111);color:#fff;font-size:9.5px;font-weight:700;border-radius:3px;display:flex;align-items:center;justify-content:center}
</style>
</head>
<body>

<div class="abs topbar"></div>
<svg class="abs home-icon" width="24" height="20" viewBox="0 0 24 20"><path d="M12 1 L23 10 L20 10 L20 19 L4 19 L4 10 L1 10 Z" fill="#c8281a"/></svg>
<div class="abs menu-btn menu-welcome">Welcome Menu <i></i></div>
<div class="abs menu-btn menu-church">Church Menu <i></i></div>
<nav class="abs nav"><a>UCW News</a><a>RVC News</a><a>Events</a><a>Employment</a></nav>
<div class="abs social">
  <span style="background:#e8792a"></span><span style="background:#3a7fc4"></span><span style="background:#e3b21e"></span><span style="background:#3cb4e6"></span><span style="background:#3b5ea8"></span><span style="background:#c0281e"></span>
</div>

<div class="abs redband"></div>
<div class="abs hero" role="img" aria-label="Photograph of smiling schoolchildren in green uniforms lining up outside a brick school">
  <div class="hero-caption">Changing lives all over North Texas...</div>
</div>
<div class="abs dots"><span></span><span></span><span></span><span></span><span></span><span></span></div>
<div class="abs bubble bubble-home">Home</div>
<div class="abs bubble bubble-tour">Site Tutorial</div>

<div class="abs band"></div>
<div class="abs tile" style="left:225px"><div class="pic" role="img" aria-label="Hands reaching through a barred window" style="background:radial-gradient(ellipse at 50% 60%,#b08a62,#6a4a2e 55%,#2e1e12)"></div><div class="label center">I NEED HELP...</div></div>
<div class="abs tile" style="left:354px"><div class="pic" role="img" aria-label="Person raising open hands in prayer" style="background:radial-gradient(ellipse at 60% 70%,#c89a3a,#8a5a38 25%,#f4f2ee 55%,#ffffff)"></div><div class="label center">I NEED GOD...</div></div>
<div class="abs tile" style="left:482px"><div class="pic" role="img" aria-label="Young woman praying quietly outdoors" style="background:radial-gradient(ellipse at 65% 55%,#d8b8a0,#a07a62 35%,#6a7a52 70%,#4a5a3a)"></div><div class="label center">I NEED A CHURCH...</div></div>
<div class="abs tile" style="left:613px"><div class="pic" role="img" aria-label="Smiling couple carrying moving boxes" style="background:radial-gradient(ellipse at 55% 60%,#c8a070,#e8dccc 40%,#6a5a4a 80%)"></div><div class="label">MOVING TO<br>NORTH TEXAS</div></div>
<div class="abs tile" style="left:742px"><div class="pic" role="img" aria-label="White church building with steeple under blue sky" style="background:linear-gradient(#2e5fa8,#8aaed8 35%,#f2f2f2 55%,#c8c8c8 70%,#4a7a32)"></div><div class="label">WHAT IS METHODIST<br>CHURCH?</div></div>
<div class="abs tile" style="left:870px"><div class="pic" role="img" aria-label="Volunteers with a red banner in front of a brick home" style="background:linear-gradient(#6a9ad8,#b07060 40%,#c02020 62%,#5a8a3a)"></div><div class="label center">I WANT TO SERVE</div></div>

<section class="abs panel"><div class="panel-head">Welcome North Texas!  Find your place!</div></section>
<svg class="abs arrow" style="left:230px" width="12" height="40" viewBox="0 0 12 40"><path d="M10 2 L2 20 L10 38" fill="none" stroke="#bbb" stroke-width="2"/></svg>
<svg class="abs arrow" style="left:961px" width="12" height="40" viewBox="0 0 12 40"><path d="M2 2 L10 20 L2 38" fill="none" stroke="#bbb" stroke-width="2"/></svg>

<div class="abs card" style="left:250px">
  <div class="frame"><div class="pic" role="img" aria-label="Group of smiling teenage friends" style="background:linear-gradient(90deg,#c88a68,#5a3424 30%,#e0b090 55%,#f0d8a8 75%,#b07850)"><div class="tag">I'M A YOUTH</div></div></div>
  <svg class="learn" width="93" height="25" viewBox="0 0 93 25"><path d="M0 0 H84 L93 12.5 L84 25 H0 Z" fill="#3a3a3a"/><text x="18" y="16" fill="#fff" font-family="Arimo,Arial,sans-serif" font-size="8.5">LEARN MORE</text></svg>
  <div class="connect">Connect : <span class="g">Gathernet</span> | <span class="c">Chirper</span></div>
</div>
<div class="abs card" style="left:428px">
  <div class="frame"><div class="pic" role="img" aria-label="Young adults laughing together" style="background:linear-gradient(90deg,#3a2a22,#c8a088 30%,#6a4a38 55%,#e8d0b0 80%,#b89070)"><div class="tag">I'M YOUNG ADULTS</div></div></div>
  <svg class="learn" width="93" height="25" viewBox="0 0 93 25"><path d="M0 0 H84 L93 12.5 L84 25 H0 Z" fill="#3a3a3a"/><text x="18" y="16" fill="#fff" font-family="Arimo,Arial,sans-serif" font-size="8.5">LEARN MORE</text></svg>
  <div class="connect">Connect : <span class="g">Gathernet</span> | <span class="c">Chirper</span></div>
</div>
<div class="abs card" style="left:607px">
  <div class="frame"><div class="pic" role="img" aria-label="Parent reading with a young daughter" style="background:linear-gradient(90deg,#2a1e18,#d8b098 35%,#4a3020 55%,#f2dcc8 75%,#f6f2ee)"><div class="tag">I HAVE KIDS</div></div></div>
  <svg class="learn" width="93" height="25" viewBox="0 0 93 25"><path d="M0 0 H84 L93 12.5 L84 25 H0 Z" fill="#3a3a3a"/><text x="18" y="16" fill="#fff" font-family="Arimo,Arial,sans-serif" font-size="8.5">LEARN MORE</text></svg>
  <div class="connect">Connect : <span class="g">Gathernet</span> | <span class="c">Chirper</span></div>
</div>
<div class="abs card" style="left:787px">
  <div class="frame"><div class="pic" role="img" aria-label="Older adults gathered together smiling" style="background:linear-gradient(90deg,#d8c8b8,#a88470 30%,#e8e0d8 50%,#7a8ab0 65%,#c8a890 85%,#efe8e0)"><div class="tag">OLDER ADLULTS</div></div></div>
  <svg class="learn" width="93" height="25" viewBox="0 0 93 25"><path d="M0 0 H84 L93 12.5 L84 25 H0 Z" fill="#3a3a3a"/><text x="18" y="16" fill="#fff" font-family="Arimo,Arial,sans-serif" font-size="8.5">LEARN MORE</text></svg>
  <div class="connect">Connect : <span class="g">Gathernet</span> | <span class="c">Chirper</span></div>
</div>

<div class="abs footbar"></div>
<div class="abs nearest">NEAREST<br>LOCATION?</div>
<div class="abs locate"><i></i>Church Online</div>
<div class="abs globe">
  <svg width="35" height="21" viewBox="0 0 35 21"><circle cx="15" cy="10.5" r="6" fill="#777"/><path d="M25 12 L28 8 L31 12 Z" fill="#c23418"/></svg>
</div>
<div class="abs community">CONNECT WITH OUR COMMUNITY ON<b>gathernet</b></div>
<div class="abs account">Register | Lost pass?</div>
<div class="abs signin">Sign In</div>

<footer class="abs foot"></footer>
<div class="abs brand"><span></span>Northfield</div>
<div class="abs divider"></div>
<div class="abs col" style="left:293px"><h4>Category</h4>Commonly Used Link<br>Commonly Used Link<br>Commonly Used Link<br>Commonly Used Link<br>Commonly Used Link</div>
<div class="abs col" style="left:413px"><h4>Category</h4>Commonly Used Link<br>Commonly Used Link<br>Commonly Used Link<br>Commonly Used Link<br>Commonly Used Link</div>
<div class="abs col" style="left:533px"><h4>Category</h4>Commonly Used Link<br>Commonly Used Link<br>Commonly Used Link<br>Commonly Used Link<br>Commonly Used Link</div>
<div class="abs col" style="left:652px"><h4>Category</h4>Commonly Used Link<br>Commonly Used Link<br>Commonly Used Link<br>Commonly Used Link<br>Commonly Used Link</div>
<div class="abs suggest">Suggestion Box</div>
<div class="abs msg">Message here</div>
<div class="abs send">Send</div>

</body>
</html>
```